Flyer Design Project for a Seminar "Crossing The Bridge Ahead"

QTVM Chartered Accountants would like a flyer invitation designed for our upcoming seminar "Crossing The Bridge Ahead." The invitation should be created in MS Word, for editing capabilities on our end.

Seminar Title: "Crossing The Bridge Ahead: Securing and Growing Worth Through An Ownership Shift"

This is a complimentary breakfast seminar for Owners and CEOs of private corporations with revenues ranging from $2M to $150M.

Please leave substantial room to enter overview information on the seminar and topics of discussion.

We are open to bold colours and interesting graphics.

An example of a very amateur in-house design is attached.

Target Market(s)

Business owners and CEOs (typically men between 40 and 50 years old)

Industry/Entity Type

Business

Requirements
Must have
• -Substantial space to enter overview info about the seminar
-Space to enter logistical info about the seminar (i.e When, Where and RSVP info)
-Text should be Gill Sans. 1 page only
Should not have
• Stock photos of fake office people or American dollars (we are a Canadian company)!

```html
<!DOCTYPE html>
<html lang="en">
<head>
<meta charset="utf-8">
<title>Crossing The Bridge Ahead – Seminar Invitation</title>
<link rel="stylesheet" href="https://fonts.googleapis.com/css2?family=Syncopate:wght@400;700&family=PT+Sans:wght@400;700&display=swap">
<style>
  :root {
    --ink: #3a3a3a;
    --orange: #f7a23a;
    --orange-deep: #f08a1c;
    --olive: #a9a31a;
    --red: #d8262e;
    --red-deep: #a8151c;
    --tag-light: #fbeeee;
    --tag-mid: #f2d2d2;
    --tag-text: #b58f8f;
    --navy: #1f3d7a;
    --bar-blue: #1aa3dc;
    --bar-red: #e5202a;
    --bar-green: #8cc63f;
    --bar-orange: #f7941d;
    --bar-yellow: #fff200;
    --bar-tan: #c49a6c;
  }
  html, body { margin: 0; padding: 0; overflow: hidden; background: #fff; }
  .flyer {
    position: relative; width: 1200px; height: 927px; overflow: hidden;
    background: #fff; font-family: "Syncopate", sans-serif; color: var(--ink);
  }
  .title-banner {
    position: absolute; left: 132px; top: 52px; width: 551px; height: 65px;
    background: var(--orange); border-radius: 14px;
    display: flex; align-items: center; justify-content: center;
  }
  .title-banner h1 {
    margin: 0; font-size: 24px; font-weight: 400; letter-spacing: 3px;
    color: #fff; white-space: nowrap;
  }
  .subtitle {
    position: absolute; left: 68px; width: 674px; top: 128px; margin: 0;
    text-align: center; font-size: 15px; font-weight: 700; line-height: 22px;
    color: var(--olive); letter-spacing: 1.5px;
  }
  .line {
    position: absolute; margin: 0; font-size: 9.6px; white-space: nowrap;
    text-transform: uppercase; letter-spacing: 0.3px; line-height: 14px;
  }
  .centered { left: 68px; width: 674px; text-align: center; }
  .left { left: 68px; }
  .topic { left: 112px; }
  .bullet {
    position: absolute; left: 94px; width: 7px; height: 7px; background: var(--orange-deep);
  }
  .details { position: absolute; left: 800px; top: 0; }
  .detail { position: absolute; left: 0; width: 340px; height: 80px; }
  .detail .tag {
    position: absolute; left: 40px; top: 6px; width: 285px; height: 66px;
    border-radius: 0 16px 16px 0;
    background: linear-gradient(90deg, var(--tag-mid), var(--tag-light) 60%, #fff);
    box-shadow: 0 1px 3px rgba(0,0,0,0.15);
  }
  .detail .tag p {
    margin: 0; position: absolute; left: 42px; top: 12px;
    font-size: 8px; line-height: 14px; color: var(--tag-text);
    text-transform: uppercase; white-space: nowrap;
  }
  .detail svg { position: absolute; left: 0; top: 0; }
  .detail .label {
    position: absolute; left: 0; top: 0; width: 84px; height: 78px;
    display: flex; align-items: center; justify-content: center;
    font-family: "PT Sans", sans-serif; font-size: 19px; color: #fff;
  }
  .signpost {
    position: absolute; left: 885px; top: 570px; width: 195px; height: 315px;
    background: linear-gradient(180deg, #f6b14a 0%, #9fcf5a 40%, #d9dcdf 70%, #b7bcc1 100%);
    border-radius: 6px;
  }
  .brand { position: absolute; top: 815px; display: flex; align-items: center; }
  .brand-qtvm { left: 205px; }
  .brand-qtvm .mark { width: 16px; height: 16px; background: #111; margin-right: 8px; }
  .brand-qtvm span { font-size: 22px; font-weight: 700; color: #111; }
  .brand-harlow { left: 442px; top: 826px; }
  .brand-harlow span { font-size: 15px; font-weight: 400; color: var(--navy); white-space: nowrap; }
  .colour-bar { position: absolute; top: 884px; height: 21px; }
</style>
</head>
<body>
<main class="flyer">
  <header class="title-banner"><h1>CROSSING THE BRIDGE AHEAD</h1></header>
  <h2 class="subtitle">SECURING AND GROWING WORTH<br>THROUGH AN OWNERSHIP SHIFT</h2>

  <p class="line centered" style="top:203px">A complimentary breakfast seminar for owners and CEOs of private</p>
  <p class="line centered" style="top:230px">corporations with revenues ranging from $2M to $150M.</p>
  <p class="line centered" style="top:258px">Thursday, February 24, 2011</p>
  <p class="line centered" style="top:283px">7:45 – 10:00 AM</p>

  <p class="line left" style="top:343px">Almost two-thirds of independent business owners in Canada are planning to</p>
  <p class="line left" style="top:369px">exit their business within the next decade. The spoils will go to those who have</p>
  <p class="line left" style="top:396px">planned in advance. Are you one of them?</p>
  <p class="line left" style="top:425px">Join Martin Arlow, partner at QTVM Chartered Accountants and Neil Varden,</p>
  <p class="line left" style="top:453px">co-founder of Harlow Capital Partners, for a compelling overview of one of</p>
  <p class="line left" style="top:481px">the most critical issues affecting privately-held businesses today.</p>
  <p class="line left" style="top:509px">Topics of discussion will include:</p>

  <span class="bullet" style="top:550px"></span>
  <p class="line topic" style="top:546px">The alternatives for exiting a business and the implications of each</p>
  <span class="bullet" style="top:580px"></span>
  <p class="line topic" style="top:576px">Tax minimization strategies for the sale/transfer of your business</p>
  <span class="bullet" style="top:612px"></span>
  <p class="line topic" style="top:608px">Tactics for gaining control of the deal to achieve a successful sale and</p>
  <p class="line topic" style="top:638px">maximize the value you receive from it</p>
  <span class="bullet" style="top:675px"></span>
  <p class="line topic" style="top:671px">Real-life case studies and lessons to be learned from them</p>

  <p class="line left" style="top:717px">All attendees will receive detailed seminar handouts and a complimentary</p>
  <p class="line left" style="top:746px">consultation with both Martin and Neil to map out the next steps in</p>
  <p class="line left" style="top:773px">developing an effective exit plan for their business.</p>

  <section class="details" aria-label="Event details">
    <div class="detail" style="top:170px">
      <div class="tag"><p>Thursday, February 24, 2011<br>7:45 – 10:00 AM</p></div>
      <svg width="84" height="78" viewBox="0 0 84 78" aria-hidden="true">
        <circle cx="42" cy="39" r="37" fill="#fff"/>
        <circle cx="42" cy="39" r="33" fill="var(--red)"/>
        <path d="M12 28 A33 33 0 0 1 72 24 L42 39 Z" fill="var(--red-deep)" opacity="0.35"/>
      </svg>
      <div class="label">When</div>
    </div>
    <div class="detail" style="top:272px">
      <div class="tag"><p>QTVM Chartered Accountants<br>4100 Lakeview Street, Suite 12<br>Toronto</p></div>
      <svg width="84" height="78" viewBox="0 0 84 78" aria-hidden="true">
        <circle cx="42" cy="39" r="37" fill="#fff"/>
        <circle cx="42" cy="39" r="33" fill="var(--red)"/>
        <path d="M12 28 A33 33 0 0 1 72 24 L42 39 Z" fill="var(--red-deep)" opacity="0.35"/>
      </svg>
      <div class="label">Where</div>
    </div>
    <div class="detail" style="top:369px">
      <div class="tag"><p>Reply by February 18, 2011<br>events@qtvmca.ca</p></div>
      <svg width="84" height="78" viewBox="0 0 84 78" aria-hidden="true">
        <circle cx="42" cy="39" r="37" fill="#fff"/>
        <circle cx="42" cy="39" r="33" fill="var(--red)"/>
        <path d="M12 28 A33 33 0 0 1 72 24 L42 39 Z" fill="var(--red-deep)" opacity="0.35"/>
      </svg>
      <div class="label">RSVP</div>
    </div>
    <div class="detail" style="top:464px">
      <div class="tag"><p>Pre-registration is required.<br>Seats are limited and will be reserved<br>on a first-come, first-served basis.</p></div>
      <svg width="84" height="78" viewBox="0 0 84 78" aria-hidden="true">
        <circle cx="42" cy="39" r="37" fill="#fff"/>
        <circle cx="42" cy="39" r="33" fill="var(--red)"/>
        <path d="M12 28 A33 33 0 0 1 72 24 L42 39 Z" fill="var(--red-deep)" opacity="0.35"/>
      </svg>
      <div class="label">Remark</div>
    </div>
  </section>

  <div class="signpost" role="img" aria-label="Illustration of a signpost with colourful arrow signs reading Exit pointing in different directions"></div>

  <div class="brand brand-qtvm"><span class="mark"></span><span>QTVM</span></div>
  <div class="brand brand-harlow"><span>HARLOW CAPITAL PARTNERS</span></div>

  <div class="colour-bar" style="left:68px;width:117px;background:var(--bar-blue)"></div>
  <div class="colour-bar" style="left:185px;width:223px;background:var(--bar-red)"></div>
  <div class="colour-bar" style="left:408px;width:248px;background:var(--bar-green)"></div>
  <div class="colour-bar" style="left:656px;width:222px;background:var(--bar-orange)"></div>
  <div class="colour-bar" style="left:878px;width:165px;background:var(--bar-yellow)"></div>
  <div class="colour-bar" style="left:1043px;width:93px;background:var(--bar-tan)"></div>
</main>
</body>
</html>
```